依頼詳細
制作条件は下記の通り。
1)スマホのトップページのデザイン。ただしトップページ全体の制作は不要で、原則は最初に表示される画面のみでよい。ただしデザインをよりわかりやすくするために、最初に表示される画面に加えてその下部の若干のデザインを含むのは自由。
2)ロゴは添付のデータを用いる。
3)指定色のレッドをブランドカラーとして強調し、サイト名の中にある「+」を象徴的に使うことが望ましい。
4)既存マッチングサイトとは一線を画する、斬新なイメージであること。
5)都会的で洗練されたデザインであるとともに、見た目の美しさだけのレベルにとどまらず、「おー!」と見た人を驚かせるようなインパクトのあるデザインであること。
6)モデル撮影やレンタルフォトの使用なども可能。その場合はダミーのイメージを置いておく。
7)キャッチコピーがあったほうがよい場合はダミーのコピーを置いておく。
8)デザインは添付の「スマホ画面」の画面にレイアウトして、JPEGデータで提出。
ページ数
1ページ
希望イメージ
シンプル 複雑
単色 カラフル
暗い 明るい
日常 高級
遊び心 厳粛
未来的 伝統的
女性的 男性的
希望する色
赤系
補足説明
最終納品はイラストレーター形式ですが、応募はJPEGにてお願いします。
添付の「スマホ画面」の画面にレイアウトしてください。
たくさんの応募をいただきましたが、従来のマッチングサイトとは異なる「斬新」「サプライズ」という点で該当するものがあまりありませんでした。
つきましては、期間延長をさせていだきますので、この点をご理解をいただき私たちを「あっ!」っと言わせるような作品を応募いただけることを願っております。
■ 選んだ理由

シンプルで操作性に秀でた作品だと感じました。

■ 提案者全員のお礼・コメント

みなさま、
たくさんの素敵な作品をありがとうございました!

```html
<!DOCTYPE html>
<html lang="ja">
<head>
<meta charset="utf-8">
<title>えにし トップ</title>
<link href="https://fonts.googleapis.com/css2?family=Noto+Sans+JP:wght@400;500;700&display=swap" rel="stylesheet">
<style>
  :root {
    --brand-red: #b5182b;
    --cta-red: #d7101c;
    --cta-red-light: #ec3a3f;
    --panel-pink: rgba(255, 255, 255, 0.28);
    --chip-red: #9c1424;
    --white: #ffffff;
    --ink: #2a1216;
    --hero-bg: #fdf5f6;
    --select-border: #d9b7bc;
  }
  * { box-sizing: border-box; margin: 0; padding: 0; }
  html, body { width: 1200px; height: 2216px; overflow: hidden; }
  body {
    font-family: "Noto Sans JP", sans-serif;
    background: var(--white);
    color: var(--ink);
    position: relative;
  }

  /* Header */
  .site-header {
    position: absolute; left: 0; top: 0; width: 1200px; height: 330px;
    background: var(--brand-red);
  }
  .brand {
    position: absolute; left: 90px; top: 92px;
    display: flex; align-items: center; gap: 24px;
    color: var(--white);
    font-family: "Noto Sans JP", sans-serif; font-weight: 500;
    font-size: 62px; line-height: 1;
  }
  .brand-dot {
    width: 64px; height: 64px; border-radius: 50%;
    background: var(--white);
  }
  .header-icons {
    position: absolute; right: 80px; top: 60px;
    display: flex; flex-direction: column; align-items: center; gap: 22px;
  }

  /* Hero */
  .hero {
    position: absolute; left: 0; top: 330px; width: 1200px; height: 1140px;
    background: linear-gradient(180deg, var(--hero-bg) 0%, #ffffff 60%, #fff0f2 100%);
  }
  .hero-photo {
    position: absolute; border-radius: 50%;
    border: 12px solid var(--white);
    box-shadow: 0 10px 30px rgba(120, 20, 30, 0.18);
  }
  .hero-photo--couple {
    left: 40px; top: 180px; width: 620px; height: 650px;
    background: radial-gradient(circle at 50% 40%, #e9d6cc 0%, #b9a299 55%, #6d5a55 100%);
  }
  .hero-photo--bride {
    left: 660px; top: 30px; width: 470px; height: 480px;
    background: radial-gradient(circle at 50% 45%, #f3ece8 0%, #c9bab2 55%, #7f6f6a 100%);
  }

  .cta-register {
    position: absolute; left: 150px; top: 965px; width: 900px; height: 150px;
    border-radius: 75px;
    background: linear-gradient(180deg, var(--cta-red-light) 0%, var(--cta-red) 55%, #b80d18 100%);
    color: var(--white);
    font-size: 62px; font-weight: 700; letter-spacing: 3px;
    display: flex; align-items: center; justify-content: center;
    box-shadow: 0 8px 18px rgba(120, 10, 20, 0.3);
  }

  /* Search panel */
  .search-area {
    position: absolute; left: 0; top: 1470px; width: 1200px; height: 746px;
    background: var(--brand-red);
  }
  .search-form {
    position: absolute; left: 115px; top: 70px; width: 970px; height: 540px;
    background: var(--panel-pink);
    border-radius: 18px;
    padding: 50px 60px;
  }
  .search-row { display: flex; align-items: center; height: 130px; }
  .search-label { width: 190px; font-size: 52px; font-weight: 500; color: var(--ink); }
  .gender-chip {
    width: 300px; height: 96px; margin-right: 40px;
    background: var(--chip-red); color: var(--white);
    display: flex; align-items: center; justify-content: center; gap: 14px;
    font-size: 52px; font-weight: 500;
  }
  .select-box {
    height: 96px; background: var(--white);
    border: 3px solid var(--select-border);
    display: flex; align-items: center; justify-content: space-between;
    padding: 0 20px 0 24px; font-size: 50px;
  }
  .select-box--age { width: 270px; }
  .select-box--area { width: 620px; }
  .tilde { width: 80px; text-align: center; font-size: 52px; }

  .try-search {
    position: absolute; left: 270px; top: 632px; width: 660px; height: 96px;
    border-radius: 48px; background: var(--white);
    border: 4px solid #e8c3c8;
    display: flex; align-items: center; justify-content: center; gap: 24px;
    font-size: 50px; font-weight: 500; color: var(--ink);
  }
</style>
</head>
<body>
  <header class="site-header">
    <div class="brand"><span class="brand-dot"></span>えにし</div>
    <div class="header-icons">
      <svg width="110" height="80" viewBox="0 0 110 80" aria-label="結婚指輪">
        <circle cx="40" cy="45" r="26" fill="none" stroke="#fff" stroke-width="7"/>
        <circle cx="70" cy="45" r="26" fill="none" stroke="#fff" stroke-width="7"/>
        <path d="M32 12 h16 l-8 10 z" fill="#fff"/>
      </svg>
      <svg width="110" height="90" viewBox="0 0 110 90" aria-label="メニュー">
        <rect x="0" y="0" width="110" height="14" fill="#fff"/>
        <rect x="0" y="38" width="110" height="14" fill="#fff"/>
        <rect x="0" y="76" width="110" height="14" fill="#fff"/>
      </svg>
    </div>
  </header>

  <section class="hero">
    <div class="hero-photo hero-photo--couple" role="img" aria-label="タキシードとドレス姿で微笑むカップルの写真"></div>
    <div class="hero-photo hero-photo--bride" role="img" aria-label="ブーケを持つ花嫁と新郎の写真"></div>
    <div class="cta-register">無料登録してはじめる</div>
  </section>

  <section class="search-area">
    <div class="search-form">
      <div class="search-row">
        <span class="search-label">お相手</span>
        <span class="gender-chip">
          <svg width="46" height="52" viewBox="0 0 46 52"><circle cx="18" cy="32" r="13" fill="none" stroke="#fff" stroke-width="5"/><path d="M27 23 L42 8 M30 7 h12 v12" fill="none" stroke="#fff" stroke-width="5"/></svg>男性</span>
        <span class="gender-chip">
          <svg width="40" height="52" viewBox="0 0 40 52"><circle cx="20" cy="17" r="12" fill="none" stroke="#fff" stroke-width="5"/><path d="M20 29 v20 M11 41 h18" stroke="#fff" stroke-width="5"/></svg>女性</span>
      </div>
      <div class="search-row">
        <span class="search-label">年齢</span>
        <span class="select-box select-box--age">30
          <svg width="44" height="34" viewBox="0 0 44 34"><path d="M0 0 h44 L22 34 z" fill="#1c0a0d"/></svg></span>
        <span class="tilde">〜</span>
        <span class="select-box select-box--age">35
          <svg width="44" height="34" viewBox="0 0 44 34"><path d="M0 0 h44 L22 34 z" fill="#1c0a0d"/></svg></span>
      </div>
      <div class="search-row">
        <span class="search-label">居住地</span>
        <span class="select-box select-box--area">関東
          <svg width="44" height="34" viewBox="0 0 44 34"><path d="M0 0 h44 L22 34 z" fill="#1c0a0d"/></svg></span>
      </div>
    </div>
    <div class="try-search">お試し検索
      <svg width="56" height="48" viewBox="0 0 56 48"><path d="M6 4 h44 a4 4 0 0 1 4 4 v24 a4 4 0 0 1 -4 4 h-26 l-12 10 v-10 h-6 a4 4 0 0 1 -4 -4 v-24 a4 4 0 0 1 4 -4z" fill="#c41a2a"/></svg>
    </div>
  </section>
</body>
</html>
```